Business card design needed

Business Card design required for new small plumbing business.
Would like a logo/text look that is simple and unique and does not have to be representative of a plumbing company (ie. having a cartoon plumber or toilet etc) as the companyname is self explanatory.
Would like the main colour to be green (lime green).
Updates

Industry/Entity Type

Plumber

Contact Information for Business Card

BRAVELL PLUMBING
ABN 61 904 127 558 003

Trevor Hasketh
Licensed Plumber 83615
Phone: 0412 870 245

27 Bravell Drive,
Kellbrook. 5972 Eastvale

Email: bravellplumbing@mailnest.example

Logo Text

Bravell Plumbing

Logo styles of interest
Character Logo
Wordmark Logo
Lettermark Logo

```html
<!DOCTYPE html>
<html lang="en">
<head>
<meta charset="utf-8">
<title>Bravell Plumbing — Business Cards</title>
<link rel="stylesheet" href="https://fonts.googleapis.com/css2?family=Cabin:wght@400;500&family=Questrial&family=Titillium+Web:wght@400;600&display=swap">
<style>
  :root {
    --stage: #545454;
    --lime: #4db848;
    --lime-light: #70c45f;
    --paper: #ffffff;
    --ink-dark: #050708;
    --wrench-light: rgba(255, 255, 255, 0.14);
    --wrench-dark: rgba(255, 255, 255, 0.07);
  }
  * { margin: 0; padding: 0; box-sizing: border-box; }
  html, body {
    width: 1200px; height: 503px; overflow: hidden;
    background: var(--stage);
  }
  .stage { position: relative; width: 1200px; height: 503px; }

  .card {
    position: absolute; top: 93px;
    width: 462px; height: 266px;
    overflow: hidden;
    box-shadow: 6px 10px 14px rgba(0, 0, 0, 0.35);
  }

  /* Light card */
  .card--light { left: 122px; background: var(--paper); }
  .card--light .band {
    position: absolute; left: 0; right: 0; top: 90px; bottom: 0;
    background: linear-gradient(to bottom, var(--lime) 0%, var(--lime) 65%, var(--lime-light) 100%);
  }
  .card--light .wordmark {
    position: absolute; top: 38px; left: 0; right: 0;
    text-align: center;
    font-family: "Questrial", sans-serif;
    font-weight: 400; font-size: 33px; line-height: 1;
    letter-spacing: 0.3px;
    color: var(--lime);
  }
  .card--light .wrench-art {
    position: absolute; left: 0; top: 78px;
    width: 156px; height: 188px;
    background: var(--wrench-light);
  }
  .card--light .holder,
  .card--light .details { color: var(--paper); font-family: "Cabin", sans-serif; }

  /* Dark card */
  .card--dark { left: 620px; background: var(--ink-dark); }
  .card--dark .wrench-art {
    position: absolute; left: 32px; top: 20px;
    width: 188px; height: 246px;
    background: var(--wrench-dark);
  }
  .card--dark .wordmark {
    position: absolute; top: 46px; left: 54px;
    font-family: "Titillium Web", sans-serif;
    font-weight: 600; font-size: 38px; line-height: 1;
    color: var(--lime);
  }
  .card--dark .holder,
  .card--dark .details { color: var(--lime); font-family: "Titillium Web", sans-serif; }

  /* Shared text blocks */
  .holder {
    position: absolute; right: 45px; top: 108px;
    font-size: 24px; line-height: 1.2;
  }
  .details {
    position: absolute; right: 45px; top: 159px;
    list-style: none; text-align: right;
    font-size: 14px; line-height: 18px;
    white-space: nowrap;
  }
  .card--dark .holder,
  .card--dark .details { right: 64px; }
</style>
</head>
<body>
<main class="stage">

  <section class="card card--light" aria-label="Business card, light version">
    <div class="band"></div>
    <div class="wrench-art" role="img" aria-label="White outline of a spanner"></div>
    <h1 class="wordmark">BRAVELL PLUMBING</h1>
    <p class="holder">Trevor Hasketh</p>
    <ul class="details">
      <li>0412 870 245 51</li>
      <li>Licensed Plumber 83615</li>
      <li>bravellplumbing@mailnest.example</li>
      <li>Bravell Drive, Kellbrook. 5972 Eastvale</li>
    </ul>
  </section>

  <section class="card card--dark" aria-label="Business card, dark version">
    <div class="wrench-art" role="img" aria-label="Faint grey outline of a spanner"></div>
    <h2 class="wordmark">Bravell Plumbing</h2>
    <p class="holder">Trevor Hasketh</p>
    <ul class="details">
      <li>0412 870 245 51</li>
      <li>Licensed Plumber 83615</li>
      <li>bravellplumbing@mailnest.example</li>
      <li>Bravell Drive, Kellbrook. 5972 Eastvale</li>
    </ul>
  </section>

</main>
</body>
</html>
```